Current wordpress website needs some additions & to be made more user friendly & visually...

Harbour Kinship Carers Network (HKCN) is a volunteer, not-for-profit organisation supporting parents & carers who are trying to support their loved one with a life-threatening eating disorder. We have a website www.hkcn.org.au which is in Wordpress & need to make membership registration & donations more obvious, streamlined, easy & efficient, as well as reducing how 'wordy' the page looks, by making it more visually appealing. Please refer to the look and feel and functionality of www.brightwatersupportcollective.org.au. Please confirm if our site can look and function as per this site.

```html
<!DOCTYPE html>
<html lang="en">
<head>
<meta charset="utf-8">
<title>Harbour Kinship Carers Network</title>
<link rel="stylesheet" href="https://fonts.googleapis.com/css2?family=Roboto:wght@400;500;700&family=Open+Sans:wght@600;700&family=Noto+Serif:ital@1&display=swap">
<style>
:root{
  --backdrop:#a9a9a9;
  --page:#f3f3f3;
  --white:#ffffff;
  --nav-bg:#f7f7f7;
  --green:#5db012;
  --green-btn:#59b246;
  --green-dark:#168a3c;
  --purple:#7b2373;
  --ink:#333333;
  --ink-dark:#1e2a12;
  --nav-ink:#555555;
}
*{margin:0;padding:0;box-sizing:border-box}
html,body{width:1200px;height:1200px;overflow:hidden;background:var(--backdrop);font-family:"Roboto",sans-serif}
.page{position:absolute;left:79px;top:0;width:1040px;height:1200px;background:var(--page);overflow:hidden}
.header{position:absolute;left:0;top:0;width:1040px;height:82px;background:var(--white)}
.btn-top{position:absolute;top:27px;height:26px;width:107px;background:var(--green-btn);color:var(--white);font-size:12px;font-weight:500;display:flex;align-items:center;justify-content:center;border-radius:2px}
.btn-donations{left:18px}
.btn-registration{right:16px}
.brand{position:absolute;left:0;width:1040px;top:5px;text-align:center}
.brand-dot{display:block;margin:0 auto 10px;width:40px;height:40px;border-radius:50%;background:var(--purple)}
.brand-name{font-size:12.5px;color:var(--ink);letter-spacing:.2px}
.nav{position:absolute;left:0;top:82px;width:1040px;height:40px;background:var(--nav-bg)}
.nav a{position:absolute;top:13px;font-size:12px;font-weight:500;color:var(--nav-ink);text-decoration:none}
.nav a.active{color:var(--green)}
.hero{position:absolute;left:0;top:122px;width:1040px;height:464px;
  background:
    radial-gradient(ellipse 260px 200px at 720px 260px,#62b444 0%,rgba(98,180,68,0) 70%),
    radial-gradient(ellipse 240px 260px at 120px 120px,#7a3a5e 0%,rgba(122,58,94,0) 70%),
    radial-gradient(ellipse 300px 240px at 520px 140px,#4e6f8f 0%,rgba(78,111,143,0) 75%),
    radial-gradient(ellipse 260px 200px at 880px 420px,#d9a78f 0%,rgba(217,167,143,0) 75%),
    linear-gradient(180deg,#9e8a7c 0%,#b89a82 55%,#a27a5c 100%)}
.hero-title{position:absolute;left:0;width:1040px;top:302px;text-align:center;font-family:"Open Sans",sans-serif;font-weight:700;font-size:35px;color:var(--white);letter-spacing:.5px}
.hero-sub{position:absolute;left:0;width:1040px;top:351px;text-align:center;font-family:"Noto Serif",serif;font-style:italic;font-size:21px;color:var(--white)}
.hero-btn{position:absolute;left:410px;top:391px;width:222px;height:31px;background:var(--green-dark);color:var(--white);font-family:"Open Sans",sans-serif;font-weight:600;font-size:13.5px;display:flex;align-items:center;justify-content:center}
.donate{position:absolute;left:68px;top:540px;width:906px;height:292px;background:var(--green);text-align:center}
.donate h2{position:absolute;left:0;width:100%;top:20px;font-size:30px;font-weight:700;color:var(--white)}
.donate-lead{position:absolute;left:0;width:100%;top:67px;font-size:20px;line-height:25.3px;color:var(--ink-dark)}
.donate-note{position:absolute;left:0;width:100%;top:185px;font-size:14.5px;color:var(--white)}
.donate-btn{position:absolute;left:348px;top:230px;width:201px;height:37px;background:var(--white);color:#111;font-weight:700;font-size:15px;letter-spacing:.3px;display:flex;align-items:center;justify-content:center}
.membership-title{position:absolute;left:0;width:1040px;top:872px;text-align:center;font-size:30px;font-weight:700;color:var(--ink)}
.membership-title span{color:var(--green)}
.tier{position:absolute;top:950px;width:250px;margin-left:-125px;text-align:center}
.tier-icon{display:block;margin:0 auto;width:86px;height:86px}
.tier-name{margin-top:26px;font-size:21px;font-weight:500;color:var(--ink);white-space:nowrap}
.tier-btn{display:flex;margin:27px auto 0;width:122px;height:35px;background:var(--green-btn);color:var(--white);font-size:15px;align-items:center;justify-content:center}
</style>
</head>
<body>
<div class="page">
  <header class="header">
    <div class="btn-top btn-donations">Donations</div>
    <div class="brand"><span class="brand-dot"></span><div class="brand-name">Harbour Kinship Carers Network</div></div>
    <div class="btn-top btn-registration">Registration</div>
  </header>
  <nav class="nav">
    <a class="active" style="left:88px">HOME</a>
    <a style="left:143px">ABOUT US</a>
    <a style="left:228px">ABOUT HKCN</a>
    <a style="left:329px">FAMILY AND CARER</a>
    <a style="left:467px">SERVICE AND CLINICIANS</a>
    <a style="left:646px">SKILLED FAMILIES</a>
    <a style="left:775px">MEMBERS</a>
    <a style="left:866px">CONTACTUS</a>
  </nav>
  <section class="hero" role="img" aria-label="Photo of a group of people at a table folding paper origami cranes, one holding a green crane"></section>
  <div class="hero-title">HOW CAN WE HELP?</div>
  <div class="hero-sub">there are so many ways..</div>
  <div class="hero-btn">Find out what we do here..</div>

  <section class="donate">
    <h2>DONATE US</h2>
    <p class="donate-lead">All donations over $2.00 to the Harbour Kinship Carers Network are tax deductable<br>and directly support people through access to counselling, practical assistance to<br>support recovery, groups, equipment for<br>the centre and books for our library.</p>
    <p class="donate-note">You can make a one-off or regular monthly donation and you will receive an automatic receipt.</p>
    <div class="donate-btn">DONATE TODAY</div>
  </section>

  <h2 class="membership-title">OUR <span>MEMBERSHIP</span></h2>

  <div class="tier" style="left:139px">
    <svg class="tier-icon" viewBox="0 0 86 86"><circle cx="43" cy="43" r="41" fill="#7b2373" stroke="#59b246" stroke-width="3"/><circle cx="38" cy="28" r="11" fill="#fff"/><path d="M20 62c0-13 8-20 18-20s14 4 16 8v12z" fill="#fff"/><circle cx="55" cy="57" r="11" fill="#fff" stroke="#7b2373" stroke-width="3"/><path d="M55 51v12M49 57h12" stroke="#7b2373" stroke-width="3"/></svg>
    <div class="tier-name">Individual Members</div>
    <div class="tier-btn">View More</div>
  </div>
  <div class="tier" style="left:398px">
    <svg class="tier-icon" viewBox="0 0 86 86"><circle cx="43" cy="43" r="41" fill="#7b2373" stroke="#59b246" stroke-width="3"/><path d="M43 18l22 8v14c0 14-9 23-22 28-13-5-22-14-22-28V26z" fill="none" stroke="#fff" stroke-width="4"/><path d="M43 27l13 5v9c0 9-6 15-13 18-7-3-13-9-13-18v-9z" fill="none" stroke="#fff" stroke-width="3"/><circle cx="43" cy="42" r="5" fill="#fff"/></svg>
    <div class="tier-name">Organisation Members</div>
    <div class="tier-btn">View More</div>
  </div>
  <div class="tier" style="left:654px">
    <svg class="tier-icon" viewBox="0 0 86 86"><circle cx="43" cy="43" r="41" fill="#7b2373" stroke="#59b246" stroke-width="3"/><path d="M30 46V30a3 3 0 016 0v12V22a3 3 0 016 0v20V20a3 3 0 016 0v22V25a3 3 0 016 0v28c0 10-6 17-15 17-6 0-10-3-13-8l-8-12a3 3 0 015-4z" fill="#fff"/></svg>
    <div class="tier-name">Members Only</div>
    <div class="tier-btn">View More</div>
  </div>
  <div class="tier" style="left:906px">
    <svg class="tier-icon" viewBox="0 0 86 86"><circle cx="43" cy="43" r="41" fill="#7b2373" stroke="#59b246" stroke-width="3"/><rect x="18" y="40" width="10" height="24" rx="2" fill="#fff"/><path d="M31 42l10-12c2-4 3-8 3-10 4 0 6 4 5 9l-2 7h13a4 4 0 014 5l-4 18a5 5 0 01-5 5H31z" fill="#fff"/></svg>
    <div class="tier-name">Renew Your Membership</div>
    <div class="tier-btn">View More</div>
  </div>
</div>
</body>
</html>
```